Brightwell Consulting Business Card Design

Business Card Design for Brightwell Consulting. Brightwell Consulting is a boutique consultancy based in Atlanta, GA., that specializes in marketing strategy, organization planning, and leadership development. We provide solutions for small businesses and startups as well as Summit 400 companies.

http://brightwellconsulting.example/

Target Market(s)

We provide solutions for small businesses and startups as well as Summit 400 companies.

Industry/Entity Type

Consulting

Contact Information for Business Card

Two sided business card with priority on contact information, logo, tag line (Inspiration to Dream More, Do More, Become More)

Colors

Designer to choose colors to be used in the design.

Requirements
Must have
• contact information, logo, tag line (Inspiration to Dream More, Do More, Become More)
• Simple no over communication.
Nice to have
• I would like to see different placements of logo and creative use of both sides of the card
Should not have
• Do not put too much information on the card.

```html
<!DOCTYPE html>
<html lang="en">
<head>
<meta charset="utf-8">
<title>Brightwell Consulting Business Card</title>
<link href="https://fonts.googleapis.com/css2?family=Open+Sans:wght@400;600;700&display=swap" rel="stylesheet">
<style>
  :root {
    --ink: #2f2f2f;
    --paper: #ffffff;
    --stage: #e9e7e4;
    --text-dark: #222222;
    --text-light: #ffffff;
  }
  * { margin: 0; padding: 0; box-sizing: border-box; }
  html, body {
    width: 1200px; height: 800px; overflow: hidden;
    background: var(--stage);
    font-family: "Open Sans", Arial, sans-serif;
  }
  .canvas {
    position: relative; width: 1200px; height: 800px;
    display: flex; align-items: center; justify-content: center; gap: 60px;
  }
  .card {
    position: relative; width: 510px; height: 292px;
    border-radius: 4px; overflow: hidden;
    box-shadow: 0 6px 18px rgba(0,0,0,0.15);
  }
  /* Front side */
  .card--front { background: var(--ink); color: var(--text-light); }
  .front__brand {
    position: absolute; left: 0; right: 0; top: 86px;
    text-align: center;
  }
  .brand-name {
    font-weight: 600; letter-spacing: 0.5px; line-height: 1.1;
  }
  .front__brand .brand-name { font-size: 46px; }
  .front__tagline {
    position: absolute; left: 0; right: 0; bottom: 40px;
    text-align: center; font-size: 15px; font-weight: 400; letter-spacing: 0.3px;
  }
  /* Back side */
  .card--back { background: var(--paper); color: var(--text-dark); }
  .back__brand {
    position: absolute; right: 34px; top: 56px; text-align: right;
  }
  .back__brand .brand-name { font-size: 30px; color: var(--text-dark); }
  .back__person { position: absolute; left: 34px; top: 104px; }
  .person__name { font-size: 19px; font-weight: 700; letter-spacing: 0.3px; }
  .person__role { font-size: 15px; margin-top: 2px; }
  .back__contact {
    position: absolute; left: 34px; top: 182px;
    list-style: none; font-size: 14px; line-height: 1.45;
  }
  .back__band { position: absolute; right: 0; bottom: 0; }
</style>
</head>
<body>
<main class="canvas">
  <section class="card card--front" aria-label="Business card front">
    <div class="front__brand">
      <p class="brand-name">Brightwell Consulting</p>
    </div>
    <p class="front__tagline">Inspiration to Dream More, Do More, Become More</p>
  </section>

  <section class="card card--back" aria-label="Business card back">
    <div class="back__brand">
      <p class="brand-name">Brightwell Consulting</p>
    </div>
    <div class="back__person">
      <p class="person__name">ALEX CARTER</p>
      <p class="person__role">Manager</p>
    </div>
    <ul class="back__contact">
      <li>555 010 247</li>
      <li>www.BrightwellConsulting.example</li>
      <li>email@BrightwellConsulting.example</li>
    </ul>
    <svg class="back__band" width="250" height="34" viewBox="0 0 250 34" aria-hidden="true">
      <polygon points="14,0 250,0 250,34 0,34" fill="var(--ink)"/>
    </svg>
  </section>
</main>
</body>
</html>
```